Corporate marketing website with signup form

The function of the website is to promote our 2 product offerings. It will contain a main screen and several 5-7 sub-pages that will be available as 'scroll down' anchors and as front-page navigation links on the top of the page.

Navigation menu labels are: Products, Unique Model, Pricing, About, and Contact

Target Market(s)

Business to business marketers who are looking to source lead generation services

Industry/Entity Type

Marketing

Logo Text

Velmora

Coding

Coded - Design and coding required

Number of Pages Required

5+ page

Requirements
Must have
• A sign-up form on main section of the front page. Fields are First Name, Last Name, Company, and Email (all text), and a pull-down with three options (only pick one): Track 1, Track 2, Custom Combination.
• Also incorporate the bottom half (ie crop the image) of the EPS file attached (the 'blue heads). Add this to the lower portion of the main screen and have the rest of the blue background become the background for the next anchored section of the navigation.
• You'll see the main section text in the mock-up I provided. The rest of the menu items/anchors can be lorem ipsum for now.
• Can this be coded in Wordpress? That would be my preference so I can edit it in the future.

```html
<!DOCTYPE html>
<html lang="en">
<head>
<meta charset="utf-8">
<title>Velmora — List and Audience Building</title>
<link href="https://fonts.googleapis.com/css2?family=Raleway:wght@400;500;600;700&family=Open+Sans:wght@400;600&display=swap" rel="stylesheet">
<style>
:root{
  --sky:#8fc0e3;
  --sky-deep:#84b9e0;
  --accent:#8bbde3;
  --bar:#5189c9;
  --ink:#222;
  --muted:#555;
  --card:#f6f6f6;
  --card-head:#e1e1e1;
  --line:#d6d6d6;
  --white:#fff;
  --btn:#7fb2de;
}
*{box-sizing:border-box;margin:0;padding:0}
html,body{width:856px;height:1200px;overflow:hidden}
body{position:relative;background:var(--white);font-family:'Open Sans',sans-serif;color:var(--ink)}
.abs{position:absolute}
a{color:inherit;text-decoration:none}

/* header */
.site-header{left:0;top:0;width:856px;height:135px;background:var(--sky)}
.brand{left:114px;top:22px;font-family:'Raleway',sans-serif;font-weight:700;font-size:29px;color:var(--white);display:flex;align-items:center;gap:8px}
.brand-dot{width:10px;height:10px;border-radius:50%;background:var(--white)}
.call{right:116px;top:32px;font-family:'Raleway',sans-serif;font-size:10px;font-weight:600;color:var(--white);display:flex;align-items:center;gap:5px}
.main-nav{right:114px;top:69px;display:flex;gap:0;font-family:'Raleway',sans-serif;font-size:9px;font-weight:500;color:var(--white)}
.main-nav a{padding:4px 8px;margin-left:7px;border:1px solid transparent}
.main-nav a.active{border-color:var(--white)}
.crowd-top{left:0;top:125px;width:856px;height:72px;background:linear-gradient(180deg,var(--sky) 0%,#b9d8ef 55%,var(--white) 100%)}

/* intro */
.intro-title{left:114px;top:244px;font-family:'Raleway',sans-serif;font-size:20px;font-weight:500}
.intro-title span{color:var(--accent)}
.intro-sub{left:115px;top:275px;font-family:'Raleway',sans-serif;font-size:12px;font-weight:500;color:var(--muted)}

.track{top:316px;width:198px;height:237px;background:var(--card);border:1px solid var(--line)}
.track-head{height:37px;background:var(--card-head);font-family:'Raleway',sans-serif;font-size:13px;font-weight:500;padding:13px 12px 0}
.track-body{padding:8px 12px}
.track-lead{font-size:10px;line-height:16px;margin-bottom:5px}
.track-copy{font-size:7.3px;line-height:13.4px;color:var(--muted);margin-bottom:14px}

.signup{left:544px;top:316px;width:197px;height:237px;background:#f1f1f1;border:1px solid var(--line)}
.signup-head{margin-left:14px;height:37px;background:var(--card-head);font-family:'Raleway',sans-serif;font-size:12.5px;font-weight:500;text-align:center;padding-top:13px}
.signup-form{padding:13px 12px 0}
.field{display:flex;height:24px;margin-bottom:4px;background:var(--white);border:1px solid #ddd}
.field-icon{width:23px;background:var(--accent);display:flex;align-items:center;justify-content:center}
.field-label{flex:1;font-size:7.4px;font-style:italic;color:#555;padding:7px 0 0 7px;position:relative}
.select-arrows{position:absolute;right:5px;top:7px}
.signup-btn{margin-top:5px;height:25px;background:var(--btn);color:var(--white);font-family:'Raleway',sans-serif;font-size:9px;font-weight:600;text-align:center;padding-top:7px}

/* products */
.crowd-mid{left:0;top:572px;width:856px;height:90px;background:linear-gradient(180deg,var(--white) 0%,#c3def2 45%,var(--sky-deep) 100%)}
.products-bg{left:0;top:660px;width:856px;height:495px;background:var(--sky-deep)}
.products-title{left:114px;top:682px;font-family:'Raleway',sans-serif;font-size:20px;font-weight:500;color:var(--white)}
.product{top:727px;width:147px;color:var(--white)}
.product-photo{width:147px;height:106px;border:1px solid var(--white)}
.product-name{font-family:'Raleway',sans-serif;font-size:14px;font-weight:500;margin-top:8px}
.product-copy{font-size:7.4px;line-height:12.8px;margin-top:5px}
.read-more{display:inline-block;margin-top:9px;border:1px solid var(--white);font-size:7.5px;padding:4px 8px}

/* footer */
.rule{left:114px;top:982px;width:627px;height:4px;border-top:1px solid #c7def2;border-bottom:1px solid #c7def2}
.foot-col{top:1014px;color:var(--white)}
.foot-head{font-family:'Raleway',sans-serif;font-size:11px;font-weight:500;margin-bottom:12px}
.foot-text{font-size:7.3px;line-height:14px}
.foot-links li{list-style:none;font-size:7.5px;line-height:15px}
.contact-row{display:flex;gap:8px;font-size:7.3px;line-height:14.5px}
.contact-row svg{flex:none;margin-top:3px}
.nl-input{width:161px;height:23px;background:var(--white);border:1px solid #ddd;font-size:7.5px;color:#444;padding:7px 9px;margin-bottom:4px}
.nl-btn{display:inline-block;background:#5a8fd0;color:var(--white);font-family:'Raleway',sans-serif;font-size:8.5px;font-weight:600;padding:7px 13px}

.bottom-bar{left:0;top:1154px;width:856px;height:46px;background:var(--bar)}
.socials{left:115px;top:1167px;display:flex;gap:4px}
.social{width:21px;height:21px;border:1.5px solid var(--white);border-radius:50%;display:flex;align-items:center;justify-content:center}
.social i{width:5px;height:5px;border-radius:50%;background:var(--white)}
.copyright{right:116px;top:1172px;font-size:7.3px;color:var(--white)}
</style>
</head>
<body>

<header class="abs site-header"></header>
<div class="abs brand"><span class="brand-dot"></span>Velmora</div>
<div class="abs call">
  <svg width="8" height="8" viewBox="0 0 10 10"><path d="M2 0.5 L3.6 2.6 L2.7 3.6 Q3.8 5.9 6.3 7.2 L7.4 6.3 L9.5 8 L8.3 9.5 Q3.5 8.8 0.5 1.8 Z" fill="#fff"/></svg>
  CALL US: 555-010-4242
</div>
<nav class="abs main-nav">
  <a class="active" href="#home">HOME</a>
  <a href="#products">PRODUCTS</a>
  <a href="#model">UNIQUE MODEL</a>
  <a href="#pricing">PRICING</a>
  <a href="#about">ABOUT</a>
  <a href="#contact">CONTACT</a>
</nav>
<div class="abs crowd-top" role="img" aria-label="Row of white audience head silhouettes against the blue header"></div>

<h1 class="abs intro-title">List And Audience Building for your <span>Content Marketing</span> Efforts</h1>
<p class="abs intro-sub">We offer 2 Track from which to choose:</p>

<section class="abs track" style="left:114px">
  <div class="track-head">TRACK <b>1</b></div>
  <div class="track-body">
    <p class="track-lead">Sed ut perspiciatis unde omnis iste nat us error sit voluptate.</p>
    <p class="track-copy">Sed ut perspiciatis unde omnis iste natus errorsit voluptatem accusantium doloremque lauda ntiu motam rem aperiam, eaque ipsa quae.</p>
    <p class="track-lead">Sed ut perspiciatis unde omnis iste nat us error sit voluptate.</p>
    <p class="track-copy">Sed ut perspiciatis unde omnis iste natus errorsit voluptatem accusantium doloremque lauda ntiu mtotam rem aperiam, eaque ips.</p>
  </div>
</section>

<section class="abs track" style="left:330px">
  <div class="track-head">TRACK <b>2</b></div>
  <div class="track-body">
    <p class="track-lead">Sed ut perspiciatis unde omnis iste nat us error sit voluptate.</p>
    <p class="track-copy">Sed ut perspiciatis unde omnis iste natus error it voluptatem accusantium doloremque laudan tiu motam rem aperiam, eaque ipsa quae.</p>
    <p class="track-lead">Sed ut perspiciatis unde omnis iste nat us error sit voluptate.</p>
    <p class="track-copy">Sed ut perspiciatis unde omnis iste natus error it voluptatem accusantium doloremque laudan tiu motam rem aperiam, eaque ipsa quae.</p>
  </div>
</section>

<section class="abs signup">
  <div class="signup-head">SIGN-UP FORM</div>
  <div class="signup-form">
    <div class="field"><span class="field-icon"><svg width="8" height="8" viewBox="0 0 10 10"><circle cx="5" cy="3" r="2.3" fill="#fff"/><path d="M1 10 Q1 5.8 5 5.8 Q9 5.8 9 10Z" fill="#fff"/></svg></span><span class="field-label">First Name:</span></div>
    <div class="field"><span class="field-icon"><svg width="8" height="8" viewBox="0 0 10 10"><circle cx="5" cy="3" r="2.3" fill="#fff"/><path d="M1 10 Q1 5.8 5 5.8 Q9 5.8 9 10Z" fill="#fff"/></svg></span><span class="field-label">Last Name:</span></div>
    <div class="field"><span class="field-icon"><svg width="7" height="8" viewBox="0 0 8 10"><rect x="0.5" y="0.5" width="7" height="9" fill="#fff"/></svg></span><span class="field-label">Company:</span></div>
    <div class="field"><span class="field-icon"><svg width="9" height="7" viewBox="0 0 10 8"><rect width="10" height="8" fill="#fff"/><path d="M0 0 L5 4.5 L10 0" stroke="#8bbde3" fill="none"/></svg></span><span class="field-label">Email:</span></div>
    <div class="field"><span class="field-icon"><svg width="9" height="8" viewBox="0 0 10 9"><path d="M0.5 0 V8.5 H10" stroke="#fff" fill="none"/><rect x="2" y="4" width="1.6" height="4" fill="#fff"/><rect x="4.5" y="2" width="1.6" height="6" fill="#fff"/><rect x="7" y="5" width="1.6" height="3" fill="#fff"/></svg></span><span class="field-label">Track:<svg class="select-arrows" width="6" height="9" viewBox="0 0 6 9"><path d="M0 3.5 L3 0 L6 3.5Z M0 5.5 L3 9 L6 5.5Z" fill="#999"/></svg></span></div>
    <div class="signup-btn">SIGN UP NOW</div>
  </div>
</section>

<div class="abs crowd-mid" role="img" aria-label="Row of blue audience head silhouettes rising into the products section"></div>
<div class="abs products-bg"></div>
<h2 class="abs products-title">Our Products</h2>

<article class="abs product" style="left:115px">
  <div class="product-photo" role="img" aria-label="Photo of colleagues working with documents at a desk" style="background:linear-gradient(135deg,#c9d4de,#6e7f90 55%,#2f3a46)"></div>
  <h3 class="product-name">Bonorum Malorum</h3>
  <p class="product-copy">Sed ut perspiciatis unde omnis istetu serror sit voluptatem accusantium dolo remque laudantium, totam rem aam, eaque ipsa quae ab illo inventore.</p>
  <a class="read-more" href="#products">READ MORE</a>
</article>
<article class="abs product" style="left:275px">
  <div class="product-photo" role="img" aria-label="Photo of printed charts, glasses and a coffee cup on a desk" style="background:linear-gradient(135deg,#3a4aa0,#c85a8a 45%,#e9e2e8 75%,#b8355a)"></div>
  <h3 class="product-name">Bonorum Malorum</h3>
  <p class="product-copy">Sed ut perspiciatis unde omnis istetu serror sit voluptatem accusantium dolo remque laudantium, totam rem aam, eaque ipsa quae ab illo inventore.</p>
  <a class="read-more" href="#products">READ MORE</a>
</article>
<article class="abs product" style="left:435px">
  <div class="product-photo" role="img" aria-label="Glowing blue and pink stock market graph" style="background:linear-gradient(135deg,#1b2d8a,#4a4fd6 45%,#d23fb0 80%,#f06ad0)"></div>
  <h3 class="product-name">Bonorum Malorum</h3>
  <p class="product-copy">Sed ut perspiciatis unde omnis istetu serror sit voluptatem accusantium dolo remque laudantium, totam rem aam, eaque ipsa quae ab illo inventore.</p>
  <a class="read-more" href="#products">READ MORE</a>
</article>
<article class="abs product" style="left:595px">
  <div class="product-photo" role="img" aria-label="Colourful stock ticker board with rising chart" style="background:linear-gradient(100deg,#1b3b8a,#1f8a5a 40%,#d6b22a 70%,#d2452e)"></div>
  <h3 class="product-name">Bonorum Malorum</h3>
  <p class="product-copy">Sed ut perspiciatis unde omnis istetu serror sit voluptatem accusantium dolo remque laudantium, totam rem aam, eaque ipsa quae ab illo inventore.</p>
  <a class="read-more" href="#products">READ MORE</a>
</article>

<div class="abs rule"></div>

<footer>
  <div class="abs foot-col" style="left:115px;width:130px">
    <h4 class="foot-head">VELMORA</h4>
    <p class="foot-text">Sed ut perspici loatis undloreme omnis isssit oluptat loem accus antiu ndeomniremqdptatem acc usan tiunde omnire.</p>
  </div>
  <div class="abs foot-col" style="left:303px">
    <h4 class="foot-head" style="margin-bottom:8px">LINKS</h4>
    <ul class="foot-links">
      <li>Home</li><li>Products</li><li>Unique Model</li><li>Pricing</li><li>About,</li><li>Contact</li>
    </ul>
  </div>
  <div class="abs foot-col" style="left:427px;width:130px">
    <h4 class="foot-head" style="margin-bottom:8px">CONTACT US</h4>
    <div class="contact-row"><svg width="6" height="7" viewBox="0 0 6 8"><path d="M3 8 L0.3 3.6 A3 3 0 1 1 5.7 3.6Z" fill="#fff"/></svg><span>Postal address: PO Box 210,<br>Larkfield sample adres lor</span></div>
    <div class="contact-row"><svg width="6" height="6" viewBox="0 0 10 10"><path d="M2 0.5 L3.6 2.6 L2.7 3.6 Q3.8 5.9 6.3 7.2 L7.4 6.3 L9.5 8 L8.3 9.5 Q3.5 8.8 0.5 1.8 Z" fill="#fff"/></svg><span>Phone: 555-010-7731</span></div>
    <div class="contact-row"><svg width="7" height="6" viewBox="0 0 8 7"><rect y="2" width="8" height="5" fill="#fff"/><rect x="2" width="4" height="2" fill="#fff"/></svg><span>Fax: 555-010-7731</span></div>
    <div class="contact-row"><svg width="7" height="5" viewBox="0 0 10 8"><rect width="10" height="8" fill="#fff"/></svg><span>hello@velmora.example</span></div>
  </div>
  <div class="abs foot-col" style="left:579px">
    <h4 class="foot-head" style="margin-bottom:4px">NEWSLETTER</h4>
    <p class="foot-text" style="font-size:8px;margin-bottom:6px">Please sign up here for latest deals</p>
    <div class="nl-input">Name:</div>
    <div class="nl-input">Email address</div>
    <span class="nl-btn">SUBSCRIBE</span>
  </div>
</footer>

<div class="abs bottom-bar"></div>
<div class="abs socials">
  <span class="social"><i></i></span><span class="social"><i></i></span><span class="social"><i></i></span><span class="social"><i></i></span>
</div>
<p class="abs copyright">© 2016 Velmora. All right reserved &nbsp;Term of Use</p>

</body>
</html>
```